Hexagon Honey Bottle Design, simple and elegant.

Bottle description:
BODY HEIGHT With cap 8.75cm
Without cap 8.6cm
DIAMETER Inner 4.4cm
Outer 5.2cm
Label height only has to be = 6cm height x (3.4X6) length of one hexagonal box is 3.4cm
See through bottle with black cap.
Concept of design:
Elegant, Simple, no pictures of bees, pictures of honeycomb, wooden honey stick, or drooling honey from either is ok. Simple colors. (Designer's discretion)
Wordings:
Hex1
Product of Yemen
Header:
MAROL /TUVI/ (Brand name)
Explanatory below header
Yemen Sidr Honey from The Valley Qarbeen (100% Pure)
(name of honey)
250g
Optional
Hex2
Pure
=
No Additives (not even natural additives)
Hex3
Raw
=
Unheated, Unpasteurized, Unprocessed honey
Hex4
Natural
=
No added color, artificial flavor, or synthetic substance
Hex5
RENOWNED
=
Very well known by honey lovers
(Natural Pure Raw and Renowned) wordings to be on a suitable place on the bottle (maybe on the cap) -
Hex6
Imported By
The Copperfield Trading Pte Ltd
No. 317, Larkspur Grove Road, #09-12
Larkspur Grove Plaza
Singapore 174593
Wordings can be rearranged - its up to the designer's discretion where and how to place them and in which order.-
Designer must be willing to do numerous changes as the design develops

```html
<!DOCTYPE html>
<html lang="en">
<head>
<meta charset="UTF-8">
<title>MAROL Honey – Hexagon Jar Label</title>
<link rel="stylesheet" href="https://fonts.googleapis.com/css2?family=Montserrat:wght@500;600;700&family=Oswald:wght@400;500&display=swap">
<style>
  :root {
    --page: #ffffff;
    --ink: #333333;
    --cream: #fdf6d2;
    --lemon: #fbe96a;
    --gold: #f9d51c;
    --amber: #f1bf0a;
    --seam: rgba(190, 150, 20, 0.18);
  }
  * { box-sizing: border-box; margin: 0; padding: 0; }
  html, body {
    width: 1200px; height: 746px; overflow: hidden;
    background: var(--page);
  }
  .canvas {
    position: relative; width: 1200px; height: 746px;
    display: flex; align-items: center; justify-content: center;
  }
  .label {
    position: relative;
    width: 1140px; height: 336px;
    display: grid; grid-template-columns: repeat(6, 1fr);
    background: linear-gradient(to bottom, var(--cream) 30%, #fcf0a8 65%, var(--lemon) 100%);
    color: var(--ink);
    box-shadow: 0 10px 30px rgba(0,0,0,0.08);
  }
  .honey-drip {
    position: absolute; left: 0; top: 0; width: 100%; height: 96px;
    pointer-events: none;
  }
  .face {
    position: relative;
    border-right: 1px solid var(--seam);
    padding: 116px 14px 18px;
    display: flex; flex-direction: column; align-items: center;
    text-align: center;
  }
  .face:last-child { border-right: none; }

  /* Hex 6 – importer */
  .face--importer { justify-content: flex-end; padding-bottom: 58px; }
  .importer {
    font-family: "Oswald", sans-serif; font-size: 9px; line-height: 1.45;
    letter-spacing: 0.01em;
  }

  /* Hex 1 – brand */
  .face--brand { padding-top: 128px; }
  .brand {
    font-family: "Montserrat", sans-serif; font-weight: 700;
    font-size: 34px; letter-spacing: 0.06em; line-height: 1;
    padding: 10px 0 8px;
    border-top: 1px solid var(--ink); border-bottom: 1px solid var(--ink);
    width: 100%;
  }
  .honey-name {
    margin-top: 52px;
    font-family: "Montserrat", sans-serif; font-weight: 600;
    font-size: 9.5px; letter-spacing: 0.08em; line-height: 1.45;
    text-transform: uppercase;
  }
  .purity {
    margin-top: 3px; padding-top: 3px;
    border-top: 1px solid var(--ink);
    font-family: "Montserrat", sans-serif; font-weight: 600;
    font-size: 11px; letter-spacing: 0.1em;
  }
  .weight {
    margin-top: auto;
    font-family: "Montserrat", sans-serif; font-weight: 600;
    font-size: 11px; letter-spacing: 0.06em;
  }

  /* Claim faces */
  .claim-title {
    font-family: "Oswald", sans-serif; font-weight: 500;
    font-size: 22px; letter-spacing: 0.02em; line-height: 1;
    padding-bottom: 5px; border-bottom: 1px solid var(--ink);
    margin-bottom: 14px;
  }
  .claim-title--wide {
    font-family: "Montserrat", sans-serif; font-weight: 700;
    font-size: 20px; letter-spacing: 0.1em;
  }
  .claim-list { list-style: none; display: flex; flex-direction: column; gap: 12px; align-self: stretch; }
  .claim-item {
    display: flex; align-items: center; gap: 6px; text-align: left;
    font-family: "Oswald", sans-serif; font-size: 10.5px; line-height: 1.15;
    text-transform: uppercase;
  }
  .claim-item small { display: block; font-size: 7px; text-transform: none; }
  .face--natural .claim-item {
    font-family: "Montserrat", sans-serif; font-weight: 500;
    font-size: 9.5px; letter-spacing: 0.08em;
  }
  .no-icon { flex: none; width: 22px; height: 22px; }
  .face--natural .no-icon { width: 28px; height: 28px; }
  .face--renowned .claim-note {
    font-family: "Oswald", sans-serif; font-size: 11px; line-height: 1.25;
    text-transform: uppercase;
  }
  .face--pure .claim-list, .face--raw .claim-list { padding-left: 10px; }
</style>
</head>
<body>
<main class="canvas">
  <section class="label">
    <svg class="honey-drip" role="img" aria-label="Band of dripping golden honey across the top of the label" viewBox="0 0 1140 96" preserveAspectRatio="none">
      <defs>
        <linearGradient id="drip-fill" x1="0" y1="0" x2="0" y2="1">
          <stop offset="0" stop-color="#f1bf0a"/>
          <stop offset="1" stop-color="#fbe14a"/>
        </linearGradient>
      </defs>
      <path fill="url(#drip-fill)" d="M0 0H1140V58C1110 62 1090 52 1060 60S1010 70 980 56 920 66 890 58 830 50 800 62 740 70 700 56 640 52 600 64 540 66 500 56 440 50 400 62 340 70 300 56 240 54 200 64 140 66 100 56 40 52 0 60Z"/>
    </svg>

    <article class="face face--importer">
      <p class="importer">Imported By:<br>The Copperfield Trading Pte Ltd<br>No. 317, Larkspur Grove Road, #09-12<br>Larkspur Grove Plaza<br>Singapore 174593</p>
    </article>

    <article class="face face--brand">
      <h1 class="brand">MAROL</h1>
      <p class="honey-name">Yemen Sidr Honey from<br>The Valley Qarbeen</p>
      <p class="purity">100% PURE</p>
      <p class="weight">250g</p>
    </article>

    <article class="face face--pure">
      <h2 class="claim-title">PURE</h2>
      <ul class="claim-list">
        <li class="claim-item">
          <svg class="no-icon" viewBox="0 0 24 24" aria-hidden="true"><circle cx="12" cy="12" r="10" fill="none" stroke="#333" stroke-width="2"/><path d="M9 7h6v10H9z" fill="none" stroke="#333" stroke-width="1.5"/><line x1="5" y1="5" x2="19" y2="19" stroke="#333" stroke-width="2"/></svg>
          <span>No Additives<small>(not even natural additives)</small></span>
        </li>
      </ul>
    </article>

    <article class="face face--raw">
      <h2 class="claim-title">RAW</h2>
      <ul class="claim-list">
        <li class="claim-item">
          <svg class="no-icon" viewBox="0 0 24 24" aria-hidden="true"><circle cx="12" cy="12" r="10" fill="none" stroke="#333" stroke-width="2"/><path d="M12 6c3 4 3 6 0 12-3-4-2-8 0-12z" fill="none" stroke="#333" stroke-width="1.5"/><line x1="5" y1="5" x2="19" y2="19" stroke="#333" stroke-width="2"/></svg>
          <span>Unheated</span>
        </li>
        <li class="claim-item">
          <svg class="no-icon" viewBox="0 0 24 24" aria-hidden="true"><circle cx="12" cy="12" r="10" fill="none" stroke="#333" stroke-width="2"/><rect x="9" y="7" width="6" height="10" rx="1" fill="none" stroke="#333" stroke-width="1.5"/><line x1="5" y1="5" x2="19" y2="19" stroke="#333" stroke-width="2"/></svg>
          <span>Unpasteurized</span>
        </li>
        <li class="claim-item">
          <svg class="no-icon" viewBox="0 0 24 24" aria-hidden="true"><circle cx="12" cy="12" r="10" fill="none" stroke="#333" stroke-width="2"/><circle cx="12" cy="12" r="4" fill="none" stroke="#333" stroke-width="1.5"/><line x1="5" y1="5" x2="19" y2="19" stroke="#333" stroke-width="2"/></svg>
          <span>Unprocessed<br>Honey</span>
        </li>
      </ul>
    </article>

    <article class="face face--natural">
      <h2 class="claim-title claim-title--wide">NATURAL</h2>
      <ul class="claim-list">
        <li class="claim-item">
          <svg class="no-icon" viewBox="0 0 24 24" aria-hidden="true"><circle cx="12" cy="12" r="10" fill="none" stroke="#333" stroke-width="1.8"/><path d="M12 6c3 4 4 6 4 8a4 4 0 0 1-8 0c0-2 1-4 4-8z" fill="none" stroke="#333" stroke-width="1.4"/><line x1="5" y1="5" x2="19" y2="19" stroke="#333" stroke-width="1.8"/></svg>
          <span>No Added Color</span>
        </li>
        <li class="claim-item">
          <svg class="no-icon" viewBox="0 0 24 24" aria-hidden="true"><circle cx="12" cy="12" r="10" fill="none" stroke="#333" stroke-width="1.8"/><path d="M8 16l6-8 2 2-6 8z" fill="none" stroke="#333" stroke-width="1.4"/><line x1="5" y1="5" x2="19" y2="19" stroke="#333" stroke-width="1.8"/></svg>
          <span>Artificial Flavor</span>
        </li>
        <li class="claim-item">
          <svg class="no-icon" viewBox="0 0 24 24" aria-hidden="true"><circle cx="12" cy="12" r="10" fill="none" stroke="#333" stroke-width="1.8"/><circle cx="9" cy="10" r="2.5" fill="none" stroke="#333" stroke-width="1.3"/><circle cx="15" cy="10" r="2.5" fill="none" stroke="#333" stroke-width="1.3"/><circle cx="12" cy="15" r="2.5" fill="none" stroke="#333" stroke-width="1.3"/></svg>
          <span>Syntheticsubstance</span>
        </li>
      </ul>
    </article>

    <article class="face face--renowned">
      <h2 class="claim-title">RENOWNED</h2>
      <p class="claim-note">Very well known<br>by honey lovers</p>
    </article>
  </section>
</main>
</body>
</html>
```